Coffee Shop needs a fresh new menu

Hi,
I would like a new menu to be designed for our coffee shop.
We display our menu on a television screen, so would need it in a file that would allow us to continue to do so -- I have attached a photo so that you can see our current design, and how it is displayed.

I'd like something that is easy to read, if the design could have a "hipster" feel to it -- we are located at a hospital and University.

I have attached a Word file with what we would like on the menu.

Feel free to contact me if you have any questions.

Thanks,
Liv

Just A4 size will be fine, and no need to include menu 1 and menu 2 - I just put them in as an example of what we already have -- they are our printed menu's. Thanks

Hospital

```html
<!DOCTYPE html>
<html lang="en">
<head>
<meta charset="utf-8">
<title>Café Menu</title>
<link rel="stylesheet" href="https://fonts.googleapis.com/css2?family=Noto+Serif:wght@400&display=swap">
<style>
  :root {
    --paper: #f4f2ef;
    --paper-glow: #fdfcfb;
    --ink: #2b2622;
    --price: #e83a8c;
    --pink: #ef4a86;
    --yellow: #f8d064;
    --swirl-soft: #ecd9e3;
    --swirl-soft-2: #efe6cf;
    --cake-tone: #e9c3cf;
    --cup-tone: #b48a64;
    --sandwich-tone: #dcb98a;
    --breakfast-tone: #e6d9c4;
  }
  * { box-sizing: border-box; margin: 0; padding: 0; }
  html, body { width: 1200px; height: 848px; overflow: hidden; }
  body {
    font-family: "Noto Serif", Georgia, serif;
    color: var(--ink);
    background: radial-gradient(ellipse at 55% 45%, var(--paper-glow) 0%, var(--paper) 70%, #e9e6e2 100%);
    position: relative;
  }
  .band { position: absolute; left: 0; width: 1200px; }
  .band--top-pink { top: 0; height: 6px; background: var(--pink); }
  .band--top-yellow { top: 9px; height: 4px; background: var(--yellow); }
  .band--bottom-yellow { bottom: 13px; height: 5px; background: var(--yellow); }
  .band--bottom-pink { bottom: 0; height: 9px; background: var(--pink); }

  .art { position: absolute; border-radius: 6px; }
  .art--swirls-top {
    left: 0; top: 13px; width: 300px; height: 390px;
    background: linear-gradient(180deg, var(--swirl-soft), var(--swirl-soft-2));
  }
  .art--swirls-bottom {
    right: 0; top: 488px; width: 235px; height: 300px;
    background: linear-gradient(180deg, var(--swirl-soft-2), var(--swirl-soft));
  }
  .art--cupcakes { left: 265px; top: 178px; width: 200px; height: 88px; background: var(--cake-tone); }
  .art--coffee-cups { left: 168px; top: 372px; width: 192px; height: 98px; background: var(--cup-tone); }
  .art--sandwich { left: 712px; top: 180px; width: 132px; height: 118px; background: var(--sandwich-tone); }
  .art--breakfast { left: 717px; top: 572px; width: 250px; height: 148px; background: var(--breakfast-tone); }

  .section { position: absolute; }
  .section__title { font-size: 21px; font-weight: 400; line-height: 1; }
  .menu-list, .coffee-list { list-style: none; font-size: 15.5px; line-height: 22.3px; white-space: nowrap; }
  .price { color: var(--price); }

  .section--light { left: 476px; top: 62px; }
  .section--light .section__title { margin-bottom: 34px; }
  .section--hot { left: 855px; top: 60px; }
  .section--hot .section__title { margin-bottom: 33px; }
  .section--breakfast { left: 476px; top: 395px; }
  .section--breakfast .section__title { margin-bottom: 33px; }
  .section--coffee { left: 36px; top: 441px; width: 420px; }
  .section--coffee .section__title { margin-bottom: 24px; }

  .coffee-list + .coffee-list { margin-top: 22px; }
  .coffee-row { position: relative; height: 22.3px; }
  .coffee-row .small, .coffee-row .large { position: absolute; top: 0; }

  .extras {
    position: absolute; left: 318px; top: 766px; width: 592px; height: 64px;
    background: var(--yellow); border-radius: 18px 18px 0 0;
    text-align: center;
  }
  .extras__title { font-size: 21px; font-weight: 400; line-height: 1; padding-top: 10px; }
  .extras__note { font-size: 15px; line-height: 1; margin-top: 6px; white-space: nowrap; }
</style>
</head>
<body>
  <div class="band band--top-pink"></div>
  <div class="band band--top-yellow"></div>

  <div class="art art--swirls-top" role="img" aria-label="Decorative ribbon swirls in pink, lilac, green and yellow"></div>
  <div class="art art--swirls-bottom" role="img" aria-label="Decorative ribbon swirls in pink, lilac, green and yellow"></div>
  <div class="art art--cupcakes" role="img" aria-label="Illustration of cupcakes"></div>
  <div class="art art--coffee-cups" role="img" aria-label="Illustration of coffee cups"></div>
  <div class="art art--sandwich" role="img" aria-label="Illustration of a sandwich"></div>
  <div class="art art--breakfast" role="img" aria-label="Illustration of a cooked breakfast"></div>

  <section class="section section--light">
    <h2 class="section__title">Something Light:</h2>
    <ul class="menu-list">
      <li>Mixed Yoghurts <span class="price">$5.50</span></li>
      <li>Chia Pudding <span class="price">$5.50</span></li>
      <li>Fruit Salad <span class="price">$5.50</span></li>
      <li>Bircher Muesli <span class="price">$5.50</span></li>
      <li>Protein Balls <span class="price">$4.0</span></li>
      <li>Banana Bread <span class="price">$4.50</span></li>
      <li>Muffins <span class="price">$4.50</span></li>
      <li>Slices <span class="price">$4.0</span></li>
    </ul>
  </section>

  <section class="section section--hot">
    <h2 class="section__title">Hot Food and Sandwiches:</h2>
    <ul class="menu-list">
      <li>Pre Made Sandwiches <span class="price">$6.50 - $7.50</span></li>
      <li>Pre Made Focaccias <span class="price">$8.50</span></li>
      <li>Wraps <span class="price">$7.50</span></li>
      <li>Vegetarian Salad <span class="price">$7.50</span></li>
      <li>Meat/Seafood Salad <span class="price">$9.50</span></li>
      <li>Hot Chips <span class="price">$4.50</span></li>
      <li>Dim Sim <span class="price">$1.50</span></li>
      <li>Potato Cake <span class="price">$1.50</span></li>
      <li>Plain Hamburger <span class="price">$7.50</span></li>
      <li>Hamburger with the lot <span class="price">$9.0</span></li>
      <li>Chicken Schnitzel Burger <span class="price">$8.50</span></li>
    </ul>
  </section>

  <section class="section section--breakfast">
    <h2 class="section__title">Breakfast Items:</h2>
    <ul class="menu-list">
      <li>Bacon, Egg and Cheese <span class="price">Roll $6.0</span></li>
      <li>Ham and Cheese Toastie <span class="price">$5.0</span></li>
      <li>Cheese and Tomato Toastie <span class="price">$5.0</span></li>
      <li>Ham and Cheese Croissant <span class="price">$6.0</span></li>
      <li>Cheese and Tomato Croissant <span class="price">$5.50</span></li>
      <li>Plain Croissant <span class="price">$3.50</span></li>
      <li>Hash Brown <span class="price">$2.0</span></li>
      <li>2 Piece Toast <span class="price">$3.0</span></li>
      <li>2 Piece Rasin Toast <span class="price">$3.0</span></li>
    </ul>
  </section>

  <section class="section section--coffee">
    <h2 class="section__title">Coffee:</h2>
    <ul class="coffee-list">
      <li class="coffee-row">Latte <span class="small" style="left:137px">small $4.0</span><span class="large" style="left:245px">Large <span class="price">$4.50</span></span></li>
      <li class="coffee-row">Cappuccino <span class="small" style="left:134px">small $4.0</span><span class="large" style="left:242px">Large <span class="price">$4.50</span></span></li>
      <li class="coffee-row">Flat White <span class="small" style="left:137px">small $4.0</span><span class="large" style="left:245px">Large <span class="price">$4.50</span></span></li>
      <li class="coffee-row">Long Black <span class="small" style="left:155px">small $4.0</span><span class="large" style="left:263px">Large <span class="price">$4.50</span></span></li>
      <li class="coffee-row">Hot Chocolate <span class="small" style="left:170px">small $4.0</span><span class="large" style="left:278px">Large <span class="price">$4.50</span></span></li>
    </ul>
    <ul class="coffee-list">
      <li class="coffee-row">Chai Latte <span class="small" style="left:133px">small $4.50</span><span class="large" style="left:254px">Large <span class="price">$5.0</span></span></li>
      <li class="coffee-row">Mocha <span class="small" style="left:133px">small $4.50</span><span class="large" style="left:242px">Large <span class="price">$5.0</span></span></li>
      <li class="coffee-row">Dirty Chai <span class="small" style="left:128px">small&nbsp; $5</span><span class="large" style="left:242px">Large <span class="price">$5.50</span></span></li>
    </ul>
    <ul class="coffee-list">
      <li>Espresso <span class="price">$3.50</span></li>
      <li>Short Macchiato <span class="price">$4.0</span></li>
      <li>Piccolo $4.0</li>
      <li>Long Macchiato <span class="price">$4.50</span></li>
    </ul>
  </section>

  <aside class="extras">
    <h2 class="extras__title">Extras</h2>
    <p class="extras__note">Soy Milk/Lactose Free Milk/Syrups/Extra Shot/Decaf&nbsp; $0.50 extra</p>
  </aside>

  <div class="band band--bottom-yellow"></div>
  <div class="band band--bottom-pink"></div>
</body>
</html>
```